Business Card Design Project

Need professional business card and Employee Badge design for a young dynamic and emp friendly IT Services company.

Target Market(s)

IT, Corporate

Industry/Entity Type

Business

Requirements
Must have
• Modern, Sleek, Prfessional, IT services
Should not have
• Too much diffrent colors

```html
<!DOCTYPE html>
<html lang="en">
<head>
<meta charset="utf-8">
<title>Talvex Technologies – Business Card</title>
<link rel="stylesheet" href="https://fonts.googleapis.com/css2?family=Exo+2:wght@600&family=Montserrat:wght@500&display=swap">
<style>
  :root {
    --page: #ffffff;
    --card: #f6f9fa;
    --rule: #2b2b2b;
    --brand: #b8333a;
    --band-start: #9c4322;
    --band-end: #d91f48;
    --accent-tan: #e6d7cc;
    --accent-grey: #e2e3e4;
    --on-band: #ffffff;
  }
  html, body {
    margin: 0;
    padding: 0;
    width: 1200px;
    height: 726px;
    overflow: hidden;
    background: var(--page);
  }
  .card {
    position: relative;
    width: 1200px;
    height: 726px;
  }
  .card-art {
    position: absolute;
    inset: 0;
    width: 1200px;
    height: 726px;
  }
  .brand-name {
    position: absolute;
    left: 92px;
    top: 210px;
    margin: 0;
    font-family: "Exo 2", sans-serif;
    font-weight: 600;
    color: var(--brand);
    line-height: 1;
  }
  .brand-name .primary {
    display: block;
    font-size: 178px;
    letter-spacing: 2px;
  }
  .brand-name .secondary {
    display: block;
    margin-top: 14px;
    font-size: 46px;
    letter-spacing: 0.62em;
    padding-left: 6px;
  }
  .website {
    position: absolute;
    left: 42px;
    width: 1119px;
    top: 629px;
    height: 65px;
    margin: 0;
    display: flex;
    align-items: center;
    justify-content: center;
    font-family: "Montserrat", sans-serif;
    font-weight: 500;
    font-size: 23px;
    letter-spacing: 0.16em;
    color: var(--on-band);
  }
</style>
</head>
<body>
  <main class="card">
    <svg class="card-art" viewBox="0 0 1075 650" preserveAspectRatio="none" aria-hidden="true">
      <defs>
        <linearGradient id="band-gradient" x1="0" y1="0" x2="1" y2="0">
          <stop offset="0" stop-color="var(--band-start)"/>
          <stop offset="1" stop-color="var(--band-end)"/>
        </linearGradient>
      </defs>
      <rect class="outer-frame" x="0.5" y="0.5" width="1074" height="649" fill="var(--page)" stroke="var(--rule)" stroke-width="1"/>
      <rect class="card-face" x="38" y="28" width="1002" height="594" fill="var(--card)" stroke="var(--rule)" stroke-width="1"/>
      <polygon class="accent-slash" points="740,488 1040,100 1040,190" fill="var(--accent-tan)"/>
      <polygon class="accent-wedge" points="740,545 1040,245 1040,545" fill="var(--accent-grey)"/>
      <rect class="footer-band" x="38" y="563" width="1002" height="59" fill="url(#band-gradient)"/>
    </svg>

    <h1 class="brand-name">
      <span class="primary">talvex</span>
      <span class="secondary">technologies</span>
    </h1>

    <p class="website">WWW.COMPANYNAME.COM</p>
  </main>
</body>
</html>
```